Premium Coffee Business Needs a Wordpress Design

We need a Wordpress design for a Premium Coffee E-commerce based in Sao Paulo, Brazil. We want something very similar to tallwillowbeans.com, but with a few exceptions, better described in the attachment (PLEASE READ our specifications). The product we're selling is premium, so we need to communicate sophistication, and at the same time people should feel they're in contact with an innovative company. Our company is called Harbor Loom.
Target Market(s)
Adults aged 25 to 50 who have refined tastes.
Industry/Entity Type
Business
Colors
Designer to choose colors to be used in the design.
Look and feel

```html
<!DOCTYPE html>
<html lang="en">
<head>
<meta charset="utf-8">
<title>Harbor Loom — Premium Coffee</title>
<link href="https://fonts.googleapis.com/css2?family=Arvo:wght@400&family=Open+Sans:wght@400;600&display=swap" rel="stylesheet">
<style>
:root{
  --red:#c3181d;
  --red-dark:#a41216;
  --white:#ffffff;
  --ink:#333333;
  --muted:#777777;
  --grey-head:#8a8a8a;
  --dark:#232323;
  --tan:#a57e5a;
  --link-red:#c9271f;
}
*{margin:0;padding:0;box-sizing:border-box}
html,body{width:1200px;height:2837px;overflow:hidden}
body{position:relative;font-family:"Open Sans",Arial,sans-serif;color:var(--ink);background:var(--white)}
.abs{position:absolute}

/* header */
.site-header{left:0;top:0;width:1200px;height:155px;background:linear-gradient(180deg,var(--red),var(--red-dark))}
.brand{left:86px;top:56px;font-family:"Arvo",Georgia,serif;font-size:48px;color:var(--white);line-height:1}
.cart{right:86px;top:30px;color:var(--white);font-size:15px;display:flex;align-items:center;gap:10px}
.main-nav{right:78px;top:90px;display:flex;gap:31px;font-size:17px;color:var(--white)}

/* hero */
.hero{left:0;top:155px;width:1200px;height:518px;background:radial-gradient(circle at 22% 45%,#e9e6e1 0 17%,transparent 18%),linear-gradient(110deg,#3b2416 0%,#5c3a22 40%,#7a5434 65%,#4a2e1b 100%)}
.hero-title{left:680px;top:318px;color:var(--white);text-transform:uppercase;line-height:1}
.hero-title .big{display:block;font-size:58px;margin-bottom:14px}
.hero-title .sub{display:block;font-size:44px;margin-bottom:16px}
.slider-dots{left:566px;top:633px;display:flex;gap:6px}
.slider-dots span{width:20px;height:20px;border-radius:50%;border:2px solid #fff;background:rgba(255,255,255,.35)}
.slider-dots span:first-child{background:#fff}

/* features */
.feature{top:760px;width:270px;text-align:center}
.feature .icon{width:126px;height:126px;border-radius:50%;margin:0 auto 30px}
.feature h3{font-weight:400;font-size:21px;color:var(--ink);margin-bottom:14px}
.feature p{font-size:14px;line-height:24px;color:var(--muted);width:210px;margin:0 auto 14px}
.feature .more{font-size:16px;color:var(--link-red)}

/* promo band */
.promo{left:0;top:1132px;width:1200px;height:423px;background:linear-gradient(100deg,#2a1c12 0%,#3f2a1b 45%,#3a3a22 75%,#25301a 100%);text-align:center;color:var(--white)}
.promo h2{position:absolute;left:0;width:1200px;top:116px;font-weight:400;font-size:42px;text-transform:uppercase}
.promo p{position:absolute;left:110px;width:980px;top:194px;font-size:15.5px;line-height:30px}
.btn-outline{position:absolute;left:525px;top:283px;width:150px;height:48px;border:1.5px solid var(--white);font-size:17px;line-height:45px;text-transform:uppercase}

/* partners */
.partners-title{left:0;width:1200px;top:1648px;text-align:center;font-size:25px;color:var(--grey-head)}
.partners{left:125px;top:1735px;width:950px;display:flex;justify-content:space-between;align-items:center}
.partner{display:flex;align-items:center;gap:12px;font-size:30px;font-weight:600;color:#3a3a3a}
.partner i{width:28px;height:28px;background:#3a3a3a;display:block}
.partner i.round{border-radius:50%}
.arrow{top:1742px}

/* gallery */
.gallery{left:0;top:1895px;width:1200px;height:690px;background:var(--dark);color:var(--white);text-align:center}
.gallery-badge{left:565px;top:1860px;width:70px;height:70px;border-radius:50%;background:var(--dark)}
.gallery h2{position:absolute;left:0;width:1200px;top:72px;font-weight:400;font-size:29px}
.gallery p{position:absolute;left:110px;width:980px;top:140px;font-size:16px;line-height:30px}
.photo{width:232px;height:154px}

/* footer */
.footer-links{left:86px;top:2628px;font-family:Arial,sans-serif;font-size:16px;color:#444}
.social{top:2620px;width:36px;height:36px}
.signup-bar{left:0;top:2685px;width:1200px;height:152px;background:var(--tan)}
.email{left:86px;top:2744px;width:273px;height:40px;background:var(--white);border-radius:3px;font-size:13px;color:#888;padding:11px 12px}
.signup-btn{left:384px;top:2744px;width:89px;height:40px;background:#3d3d3d;border-radius:3px;color:var(--white);font-size:16px;text-align:center;line-height:40px}
.legal{top:2756px;font-family:Arial,sans-serif;font-size:13px;color:var(--white)}
</style>
</head>
<body>

<header class="abs site-header">
  <div class="abs brand">Harbor Loom</div>
  <div class="abs cart">
    <svg width="22" height="20" viewBox="0 0 22 20" aria-hidden="true"><path d="M1 2h4l3 11h10l3-8H7" fill="none" stroke="#fff" stroke-width="2"/><circle cx="9" cy="17" r="2" fill="#fff"/><circle cx="17" cy="17" r="2" fill="#fff"/></svg>
    Items (0)
  </div>
  <nav class="abs main-nav"><span>Home</span><span>Brewing guides</span><span>Subscriptions</span><span>Merchandise</span><span>Our Story</span></nav>
</header>

<section class="abs hero" role="img" aria-label="White cup of coffee on a saucer beside roasted beans spilling from a burlap sack on a wooden table"></section>
<h1 class="abs hero-title"><span class="big">Coffee</span><span class="sub">The most tasty</span><span class="sub">beans on earth</span></h1>
<div class="abs slider-dots"><span></span><span></span><span></span></div>

<div class="abs feature" style="left:58px">
  <div class="icon" style="background:#e0413f" role="img" aria-label="Coffee plant icon"></div>
  <h3>Coffee Plant</h3>
  <p>Claritas est etiam processus micus, qui sequitur mutationem consuetudium lectorum</p>
  <div class="more">Read More +</div>
</div>
<div class="abs feature" style="left:328px">
  <div class="icon" style="background:#ef7a2c" role="img" aria-label="Coffee roast machine icon"></div>
  <h3>Coffee Roast Machine</h3>
  <p>Claritas est etiam processus micus, qui sequitur mutationem consuetudium lectorum</p>
  <div class="more">Read More +</div>
</div>
<div class="abs feature" style="left:603px">
  <div class="icon" style="background:#8bb46a" role="img" aria-label="Delivery truck icon"></div>
  <h3>Shipping Process</h3>
  <p>Claritas est etiam processus micus, qui sequitur mutationem consuetudium lectorum</p>
  <div class="more">Read More +</div>
</div>
<div class="abs feature" style="left:870px">
  <div class="icon" style="background:#6fb6c3" role="img" aria-label="Steaming cup of coffee icon"></div>
  <h3>Cup Of Coffee</h3>
  <p>Claritas est etiam processus micus, qui sequitur mutationem consuetudium lectorum</p>
  <div class="more">Read More +</div>
</div>

<section class="abs promo" role="img" aria-label="Roasted coffee beans and green coffee leaves on dark wood">
  <h2>Claritas est etiam processus</h2>
  <p>Claritas est etiam processus dynamicus, qui sequitur mutationem consuetudium lectorum. Mirum est notare quam littera gothica, quam nunc putamus parum claram, anteposuerit litterarum formas humanitatis per seacula quarta.</p>
  <div class="btn-outline">Shop now</div>
</section>

<div class="abs partners-title">Eodem modo typi, qui nunc nobis videntur parum clari, fiant sollemnes</div>
<svg class="abs arrow" style="left:84px" width="14" height="24" viewBox="0 0 14 24" aria-hidden="true"><path d="M12 2 2 12l10 10" fill="none" stroke="#666" stroke-width="2.5"/></svg>
<div class="abs partners">
  <div class="partner"><i></i>Northfold</div>
  <div class="partner">Mirelle Home</div>
  <div class="partner"><i class="round"></i>Basalto</div>
  <div class="partner">Vessel Works</div>
</div>
<svg class="abs arrow" style="left:1102px" width="14" height="24" viewBox="0 0 14 24" aria-hidden="true"><path d="M2 2l10 10L2 22" fill="none" stroke="#666" stroke-width="2.5"/></svg>

<section class="abs gallery">
  <h2>Podem modo typi, qui nunc nobis</h2>
  <p>Morbi tempor arcu id tellus lobortis volutpat. Suspendisse mi risus, pharetra vitae dictum eget, sodales id lacus. Vestibulum consectetur, leo sit amet sollicitudin molestie. leo sit amet sollicitudin molestie.</p>
</section>
<div class="abs gallery-badge" role="img" aria-label="Coffee bean emblem"></div>
<div class="abs photo" style="left:207px;top:2142px;background:linear-gradient(135deg,#1f3a12,#5d8a2c 60%,#8a2a1c)" role="img" aria-label="Coffee cherries on a branch"></div>
<div class="abs photo" style="left:484px;top:2142px;background:radial-gradient(circle,#9cc24a,#4f7a1c)" role="img" aria-label="Green coffee cherries"></div>
<div class="abs photo" style="left:763px;top:2142px;background:linear-gradient(160deg,#d8d2c8,#6b4528 60%,#2e1a0e)" role="img" aria-label="Roasted beans in a glass"></div>
<div class="abs photo" style="left:207px;top:2340px;background:linear-gradient(120deg,#222,#9a9a9a 50%,#3a3a3a)" role="img" aria-label="Black and white photo of a coffee cup"></div>
<div class="abs photo" style="left:484px;top:2340px;background:linear-gradient(160deg,#5a3420,#b07a4e 45%,#3a2011)" role="img" aria-label="Roasting coffee beans with steam"></div>
<div class="abs photo" style="left:763px;top:2340px;background:linear-gradient(140deg,#1d2638,#5b6b8a 50%,#c9b9a0)" role="img" aria-label="Coffee cup beside a book"></div>

<div class="abs footer-links">Contact | Special Orders | Wholesale | Press | FAQ</div>
<div class="abs social" style="left:930px;background:#3b5a9a" role="img" aria-label="Social link"></div>
<div class="abs social" style="left:978px;background:#2a9fd6" role="img" aria-label="Social link"></div>
<div class="abs social" style="left:1026px;background:#ef6b1f" role="img" aria-label="Feed link"></div>
<div class="abs social" style="left:1078px;background:#d9252a" role="img" aria-label="Video link"></div>

<footer class="abs signup-bar"></footer>
<div class="abs email">Enter Email for news updates</div>
<div class="abs signup-btn">SIGN UP</div>
<div class="abs legal" style="left:614px">Terms and Conditions | Site Map</div>
<div class="abs legal" style="left:865px">Copyright © 2013. All Rights Reserved.</div>

</body>
</html>
```